Book Cover design

The book title is Winter stayed longer in our little kitchen

I need a book cover design for a book about the unexpected loss of child. The book is a journal of my first 12 months after the loss of my son. An expression of how the grief never ends you just learn to cope. The journey to healing and hope.
Updates

Change in book title

Target Market(s)

Anyone that has experienced loss of love, career, physical loss, PTSD or experienced losing someone in an untimely manner

Font styles to use
Serif

Colors
0456a4
0792cd
33b8a4
acd136
ffffff
cee9f5
cfdeed

Requirements
Must have
• Beauty Depth

```html
<!DOCTYPE html>
<html lang="en">
<head>
<meta charset="utf-8">
<title>Winter Stayed Longer in Our Little Kitchen — Book Cover</title>
<link rel="stylesheet" href="https://fonts.googleapis.com/css2?family=Cinzel:wght@400&family=Crimson+Text&display=swap">
<style>
  :root {
    --band: #eeeeec;
    --band-edge: #e4e5e2;
    --ink: #1a1a1a;
    --canopy-deep: #0b1a10;
    --canopy: #1d3b22;
    --leaf: #3f7a34;
    --leaf-light: #79b24a;
    --lawn: #72b841;
    --hedge: #13261a;
    --path: #4a4a3c;
    --ground: #3a2c20;
    --ground-deep: #22190f;
    --bark: #5d6e5a;
    --glass: #9fc6cf;
    --white: #ffffff;
  }
  html, body {
    margin: 0;
    padding: 0;
    width: 848px;
    height: 1200px;
    overflow: hidden;
    background: var(--white);
  }
  .cover {
    position: relative;
    width: 848px;
    height: 1200px;
    overflow: hidden;
  }
  .title-band {
    position: absolute;
    left: 0;
    top: 0;
    width: 182px;
    height: 1200px;
    background: linear-gradient(90deg, var(--band) 0%, var(--band-edge) 100%);
  }
  .title {
    position: absolute;
    left: 0;
    top: 96px;
    width: 182px;
    height: 1008px;
    margin: 0;
    display: flex;
    align-items: center;
    justify-content: center;
    writing-mode: vertical-rl;
    transform: rotate(180deg);
    font-family: "Cinzel", "Trajan Pro", serif;
    font-weight: 400;
    font-size: 50px;
    line-height: 1.4;
    letter-spacing: 0.04em;
    text-transform: uppercase;
    color: var(--ink);
    text-align: center;
    white-space: nowrap;
  }
  .garden-photo {
    position: absolute;
    left: 182px;
    top: 0;
    width: 666px;
    height: 1200px;
    background:
      /* soft vignette for depth */
      radial-gradient(ellipse 75% 60% at 52% 52%, transparent 55%, rgba(5,12,7,0.55) 100%),
      /* trunk on the right edge */
      linear-gradient(90deg, transparent 0%, transparent 84%, rgba(93,110,90,0.85) 90%, rgba(40,52,38,0.9) 100%),
      /* pale glass of the house behind the trees */
      radial-gradient(ellipse 22% 9% at 56% 50%, rgba(159,198,207,0.55), transparent 75%),
      /* light breaking through the canopy */
      radial-gradient(ellipse 30% 14% at 64% 30%, rgba(121,178,74,0.55), transparent 75%),
      radial-gradient(ellipse 25% 10% at 30% 22%, rgba(121,178,74,0.35), transparent 75%),
      /* main dark branch arching across */
      radial-gradient(ellipse 60% 4% at 40% 14%, rgba(8,16,10,0.85), transparent 80%),
      radial-gradient(ellipse 55% 5% at 55% 36%, rgba(8,16,10,0.75), transparent 80%),
      /* bright lawn */
      radial-gradient(ellipse 60% 3% at 58% 61%, rgba(114,184,65,0.95), transparent 85%),
      /* gravel path */
      radial-gradient(ellipse 65% 3% at 55% 69%, rgba(110,108,92,0.55), transparent 85%),
      /* scattered-leaf ground */
      radial-gradient(ellipse 50% 14% at 60% 88%, rgba(92,68,46,0.55), transparent 80%),
      linear-gradient(180deg,
        var(--canopy) 0%,
        var(--canopy-deep) 12%,
        var(--leaf) 22%,
        var(--canopy) 32%,
        var(--canopy-deep) 38%,
        var(--leaf) 48%,
        #2c5f36 56%,
        var(--lawn) 60%,
        var(--hedge) 64%,
        var(--hedge) 66%,
        var(--path) 70%,
        var(--ground) 76%,
        var(--ground) 90%,
        var(--ground-deep) 100%);
  }
  .subtitle {
    position: absolute;
    left: 203px;
    top: 240px;
    height: 716px;
    margin: 0;
    writing-mode: vertical-rl;
    transform: rotate(180deg);
    font-family: "Crimson Text", Georgia, serif;
    font-size: 50px;
    line-height: 1;
    color: var(--white);
    white-space: nowrap;
    text-align: left;
  }
</style>
</head>
<body>
  <main class="cover">
    <div class="title-band"></div>
    <h1 class="title">Winter Stayed Longer<br>In Our Little Kitchen</h1>
    <div class="garden-photo" role="img" aria-label="Photograph of an empty rope swing hanging from a great oak branch in a quiet green garden, with a lawn, hedges and a house with tall windows behind"></div>
    <p class="subtitle">The Journey To Healing And Hope.</p>
  </main>
</body>
</html>
```